Harbourgate Earthmoving – Website Design Brief

Web Design Brief

We are seeking a web designer to build a modern, responsive website for Harbourgate Earthmoving, a Sydney-based earthworks and excavation company.

2. Project Goal
- Build a professional, easy-to-navigate website that:
- Showcases HGE’s capabilities and past projects
- Attracts residential and commercial developers
- Builds credibility and encourages enquiries

3. Target Audience
- Residential developers and home builders
- Commercial construction firms
- Project managers seeking reliable excavation & plant hire services

4. Services to Highlight
- Bulk Excavation
- Detailed Excavation
- Demolition
- Shoring
- Plant Hire

5. Brand Style & Tone
- Clean, bold, and modern
- Professional with a “we get the job done” attitude
- Colors: Lime Green + Concrete Grey (from logo)
- Fonts: Match the modern, rounded, bold typeface in the logo
- Imagery: Showcase big machines, on-site work, before & after shots

6. Website Pages
Recommended structure:
- Home – Quick intro, project highlights, CTA
- About Us – Team story, mission, safety focus
- Services – Separate sections for each core service
- Projects – Case studies or photo gallery
- Plant Hire – Machines available, specs/photos
- Contact – Form + map + details

7. Assets Provided
- Logo (both long + stacked formats)
- Project photos. More can be provided if required.
- Copy: To be drafted

8. Deliverables
Responsive website (desktop/mobile/tablet)
- SEO-ready structure
- CMS (WordPress) for future edits
- Google Maps integration, job enquiry form

Target Market(s)

Target Audience Residential developers and home builders Commercial construction firms Project managers seeking reliable excavation & plant hire services

Industry/Entity Type

Construction

Number of Pages Required

1 page

Requirements
Must have
• Build a professional, easy-to-navigate website that: Showcases HGE’s capabilities and past projects Attracts residential and commercial developers Builds credibility and encourages enquiries
Nice to have
• All provided in the Description
Should not have

```html
<!DOCTYPE html>
<html lang="en">
<head>
<meta charset="utf-8">
<title>Harbourgate Earthmoving</title>
<link href="https://fonts.googleapis.com/css2?family=Michroma&family=Poppins:wght@400;500;600;700&display=swap" rel="stylesheet">
<style>
:root{
  --lime:#8bc34a;
  --lime-dark:#7cb342;
  --black:#111111;
  --charcoal:#4d4d4d;
  --concrete:#c4c4c4;
  --panel:#f2f2f2;
  --white:#ffffff;
  --text:#333333;
  --muted:#bdbdbd;
  --gold:#f5b301;
}
*{box-sizing:border-box;margin:0;padding:0}
html,body{width:1200px;height:4167px;overflow:hidden}
body{position:relative;background:var(--white);font-family:"Poppins",sans-serif;color:var(--text)}
.display{font-family:"Michroma",sans-serif;font-weight:400;text-transform:uppercase;letter-spacing:-0.5px}
section,header,footer{position:absolute;left:0;width:1200px}
.btn{position:absolute;display:flex;align-items:center;justify-content:center;font-size:11px;font-weight:600;text-transform:uppercase;background:var(--lime);color:var(--white)}
.btn-white{background:var(--white);color:var(--black)}
.photo{position:absolute}

/* header */
.site-header{top:0;height:65px;background:var(--black)}
.brand{position:absolute;font-family:"Michroma",sans-serif;color:var(--lime);font-size:11.5px;letter-spacing:0;text-transform:uppercase;white-space:nowrap}
.site-header .brand{left:121px;top:25px}
.main-nav{position:absolute;left:510px;top:25px;display:flex;font-size:11.5px;color:var(--white)}
.main-nav a{color:var(--white);text-decoration:none;margin-right:32px;padding-bottom:4px}
.main-nav a.active{font-weight:600;border-bottom:2px solid var(--lime)}
.site-header .btn{left:970px;top:16px;width:108px;height:34px;font-size:11.5px;text-transform:none}

/* hero */
.hero{top:65px;height:574px}
.hero .photo{inset:0;background:linear-gradient(160deg,#5d6a7a 0%,#a88a5e 30%,#7a5a3a 60%,#3a2a1c 100%)}
.hero h1{position:absolute;left:121px;top:155px;color:var(--white);font-size:40px;line-height:53px}
.hero .btn{left:121px;top:333px;width:130px;height:42px;font-size:10.5px}

/* deco vertical */
.deco-word{position:absolute;font-family:"Michroma",sans-serif;font-size:62px;color:#eeeeee;white-space:nowrap;text-transform:uppercase;transform-origin:left top}
.deco-left{left:0;top:1520px;transform:rotate(-90deg)}
.deco-right{left:1200px;top:640px;transform:rotate(90deg)}

/* sectors */
.sectors{top:700px;height:259px}
.sector-panel{position:absolute;top:0;height:259px;padding-top:42px;color:var(--white)}
.sector-panel h2{font-size:18px;margin-bottom:12px;white-space:nowrap}
.sector-panel p{font-size:11px;line-height:19px}
.sector-panel .btn{position:absolute;top:183px;width:171px;height:42px;font-size:11px}
.res-panel{left:316px;width:274px;background:var(--lime);padding-left:18px;padding-right:60px}
.com-panel{left:609px;width:275px;background:var(--charcoal);padding-left:55px;padding-right:18px}
.badge{position:absolute;width:96px;height:96px;border-radius:50%;background:var(--white);display:flex;align-items:center;justify-content:center;text-align:center;font-family:"Michroma",sans-serif;color:var(--lime);font-size:9px;line-height:12px;text-transform:uppercase}

/* about */
.about{top:1022px;height:437px}
.about .back{left:121px;top:0;width:341px;height:437px;background:linear-gradient(180deg,#8fb4d8 0%,#c7b08a 55%,#8a6a45 100%)}
.about .front{left:268px;top:60px;width:342px;height:317px;border:4px solid var(--white);background:linear-gradient(180deg,#d4e0ea 0%,#bfa67a 50%,#9a7a52 100%)}
.about h2{position:absolute;left:671px;top:80px;font-size:28px;color:var(--black);display:flex;align-items:center}
.about h2::after{content:"";display:block;width:82px;height:3px;background:var(--black);margin-left:10px}
.about .copy{position:absolute;left:671px;top:125px;width:406px;font-size:11px;line-height:18.5px}
.about .copy p{margin-bottom:14px}
.about .btn{left:671px;top:307px;width:131px;height:42px;font-size:10.5px}

/* services */
.services{top:1520px;height:666px;background:var(--concrete)}
.section-title{position:absolute;left:0;width:1200px;text-align:center;font-size:29px;color:var(--black)}
.services .section-title{top:58px}
.service-card{position:absolute;width:308px;height:201px;background:var(--panel);text-align:center;padding-top:72px}
.service-card h3{font-size:17px;font-weight:600;color:var(--black);text-transform:uppercase;margin-bottom:8px}
.service-card p{font-size:11px;line-height:18px;padding:0 28px}
.service-card .more{display:block;margin-top:6px;font-size:10.5px;font-weight:600;color:var(--black);text-transform:uppercase}
.service-card .icon{position:absolute;left:116px;top:-26px;width:76px;height:76px;border-radius:50%;background:var(--lime);border:4px solid var(--white);display:flex;align-items:center;justify-content:center}
.service-card.featured{background:linear-gradient(180deg,#4a5563 0%,#6b5d4a 100%);color:var(--white)}
.service-card.featured .icon{background:var(--black)}
.service-card.featured h3,.service-card.featured p{color:var(--white)}
.service-card.featured .more{color:var(--lime)}
.service-card.cta{background:var(--lime);color:var(--white);padding-top:48px}
.service-card.cta .small{font-size:13px}
.service-card.cta h3{color:var(--white);font-size:20px;line-height:27px;margin:2px 0 10px}
.service-card.cta .btn{position:static;margin:0 auto;width:130px;height:42px;font-size:11px}

/* testimonials */
.testimonials{top:2186px;height:450px}
.testimonials .photo{inset:0;background:linear-gradient(180deg,#2d2e2c 0%,#3c3a35 50%,#262624 100%)}
.testimonials .section-title{top:58px;color:var(--white)}
.review{position:absolute;top:147px;width:308px;height:238px;background:var(--white);border-bottom:4px solid var(--lime);padding:32px 32px 0 32px}
.review .avatar{position:absolute;left:32px;top:32px;width:50px;height:50px;border-radius:50%;background:linear-gradient(180deg,#d9d9d9,#a8a8a8)}
.review .stars{margin-left:62px;color:var(--gold);font-size:13px;letter-spacing:1px;line-height:16px}
.review h4{margin-left:62px;font-size:12.5px;font-weight:700;color:var(--black);text-transform:uppercase;margin-top:6px}
.review p{margin-top:24px;font-size:11px;line-height:19px}

/* gallery */
.gallery{top:2636px;height:792px}
.gallery .section-title{top:58px}
.tile{position:absolute}
.tile span{position:absolute;left:0;top:0;background:#3a3a3a;color:var(--white);font-size:13.5px;font-weight:600;text-transform:uppercase;padding:9px 22px}
.gallery .btn{left:527px;top:694px;width:159px;height:42px;font-size:11px}

/* cta band */
.cta-band{top:3428px;height:262px;background:var(--lime);text-align:center}
.cta-band h2{position:absolute;left:0;width:1200px;top:58px;color:var(--white);font-size:29px;line-height:38px}
.cta-band .btn{left:535px;top:151px;width:130px;height:43px}

/* footer */
.site-footer{top:3690px;height:477px;background:var(--black);color:var(--white);overflow:hidden}
.site-footer .brand{left:121px;top:72px}
.site-footer .about-text{position:absolute;left:121px;top:112px;width:260px;font-size:11px;line-height:19px}
.socials{position:absolute;left:121px;top:203px;display:flex;gap:12px}
.socials span{width:22px;height:22px;border-radius:50%;border:1.5px solid var(--white)}
.foot-col{position:absolute;top:68px;font-size:11px;line-height:19px}
.foot-col h5{font-family:"Michroma",sans-serif;font-weight:400;font-size:13px;text-transform:uppercase;margin-bottom:22px;white-space:nowrap}
.foot-col ul{list-style:none}
.foot-col li{margin-bottom:11px}
.foot-col .mail{color:var(--lime);font-size:10px}
.foot-col p{margin-bottom:14px}
.news-input{width:251px;height:42px;border:1px solid var(--white);font-size:10px;padding:0 14px;display:flex;align-items:center;margin-top:12px}
.foot-col .btn{position:static;width:131px;height:42px;margin-top:16px;font-size:11px}
.copyright{position:absolute;left:0;width:1200px;top:377px;text-align:center;font-size:11px}
.foot-deco{position:absolute;left:0;top:403px;font-family:"Michroma",sans-serif;font-size:82px;color:#262626;white-space:nowrap;text-transform:uppercase}
</style>
</head>
<body>

<header class="site-header">
  <div class="brand">Harbourgate Earthmoving</div>
  <nav class="main-nav">
    <a class="active">Home</a><a>About Us ⌄</a><a>Services</a><a>Gallery</a><a>Contact Us</a>
  </nav>
  <a class="btn">Contact Us</a>
</header>

<section class="hero">
  <div class="photo" role="img" aria-label="Large wheel loader on a dirt mound at sunset"></div>
  <h1 class="display">Shaping the<br>land, building<br>the future</h1>
  <a class="btn">Get Started</a>
</section>

<div class="deco-word deco-left" aria-hidden="true">Harbourgate</div>
<div class="deco-word deco-right" aria-hidden="true">Harbourgate</div>

<section class="sectors">
  <div class="photo" style="left:121px;top:0;width:195px;height:259px;background:linear-gradient(180deg,#7fa7d0 0%,#c4cbd2 50%,#c48a2c 100%)" role="img" aria-label="Tower crane beside high-rise construction"></div>
  <div class="sector-panel res-panel">
    <h2 class="display">Residential</h2>
    <p>Lorem ipsum dolor sit amet, con sectetur adipiscing elit. Cras dapi bus vehicula tortor, maximus solli citudin ligula luctus a. Duis molesti e mauris ac nunc tincidunt</p>
    <a class="btn btn-white" style="left:18px">Residential Services</a>
  </div>
  <div class="sector-panel com-panel">
    <h2 class="display">Commercial</h2>
    <p>Lorem ipsum dolor sit amet, con sectetur adipiscing elit. Cras dapi bus vehicula tortor, maximus solli citudin ligula luctus a. Duis molesti e mauris ac nunc tincidunt</p>
    <a class="btn btn-white" style="left:55px">Commercial Services</a>
  </div>
  <div class="photo" style="left:884px;top:0;width:195px;height:259px;background:linear-gradient(180deg,#4e7fb3 0%,#c48a3a 60%,#8a4a1c 100%)" role="img" aria-label="Excavator bucket dropping soil"></div>
  <div class="badge" style="left:552px;top:82px">Harbour<br>gate</div>
</section>

<section class="about">
  <div class="photo back" role="img" aria-label="Excavator working on a site under blue sky"></div>
  <div class="photo front" role="img" aria-label="Excavator loading a dump truck with a worker nearby"></div>
  <div class="badge" style="left:214px;top:170px">Harbour<br>gate</div>
  <h2 class="display">About Us</h2>
  <div class="copy">
    <p>Lorem ipsum dolor sit amet, consectetur adipiscing elit. Cras dapibus vehicula tortor, maximus sollicitudin ligula luctus a. Duis molestie mauris ac nunc tincidunt, non fermentum mauris sollicitudin.</p>
    <p>Mauris sodales, dolor eu ultricies malesuada, mauris eros commodo felis, id venenatis ex urna a nulla. Proin dapibus vitae elit ac accumsan. In a pretium mi, at eleifend purus. Proin id sollicitudin elit. Fusce viverra augue ut magna pulvinar semper. Phasellus tempus lorem luctus leo mollis malesuada.Integer est dui, blandit sed lectus ut.</p>
  </div>
  <a class="btn">Learn More</a>
</section>

<section class="services">
  <h2 class="section-title display">Our Services</h2>

  <div class="service-card featured" style="left:121px;top:155px" role="group" aria-label="Bulk excavation, over a photo of earthworks">
    <div class="icon"><svg width="34" height="34" viewBox="0 0 34 34" fill="none" stroke="#fff" stroke-width="2"><rect x="5" y="18" width="18" height="7"/><circle cx="9" cy="28" r="2"/><circle cx="19" cy="28" r="2"/><path d="M12 18v-6h7l4 6M23 18l6-9 3 6h-4"/></svg></div>
    <h3>Bulk Excavation</h3>
    <p>Lorem ipsum dolor sit amet, consectetur adipiscing elit. Cras dapibus vehicula tortor, maximus sollicitudin ligula luctus a.</p>
    <span class="more">Learn More</span>
  </div>
  <div class="service-card" style="left:446px;top:155px">
    <div class="icon"><svg width="34" height="34" viewBox="0 0 34 34" fill="none" stroke="#fff" stroke-width="2"><rect x="10" y="8" width="12" height="12"/><rect x="6" y="20" width="22" height="6"/><circle cx="10" cy="28" r="2"/><circle cx="24" cy="28" r="2"/></svg></div>
    <h3>Detailed Excavation</h3>
    <p>Lorem ipsum dolor sit amet, consectetur adipiscing elit. Cras dapibus vehicula tortor, maximus sollicitudin ligula luctus a.</p>
    <span class="more">Learn More ›</span>
  </div>
  <div class="service-card" style="left:771px;top:155px">
    <div class="icon"><svg width="34" height="34" viewBox="0 0 34 34" fill="none" stroke="#fff" stroke-width="2"><rect x="5" y="14" width="9" height="14"/><rect x="16" y="20" width="13" height="8"/><path d="M18 20l5-10 5 4"/></svg></div>
    <h3>Demolition</h3>
    <p>Lorem ipsum dolor sit amet, consectetur adipiscing elit. Cras dapibus vehicula tortor, maximus sollicitudin ligula luctus a.</p>
    <span class="more">Learn More ›</span>
  </div>
  <div class="service-card" style="left:121px;top:403px">
    <div class="icon"><svg width="34" height="34" viewBox="0 0 34 34" fill="none" stroke="#fff" stroke-width="2"><path d="M7 6v22h22M12 12v12M17 16v8M22 20v4"/></svg></div>
    <h3>Shoring</h3>
    <p>Lorem ipsum dolor sit amet, consectetur adipiscing elit. Cras dapibus vehicula tortor, maximus sollicitudin ligula luctus a.</p>
    <span class="more">Learn More ›</span>
  </div>
  <div class="service-card" style="left:446px;top:403px">
    <div class="icon"><svg width="34" height="34" viewBox="0 0 34 34" fill="none" stroke="#fff" stroke-width="2"><rect x="8" y="14" width="18" height="14"/><path d="M13 14V8h8v6M12 20h10"/></svg></div>
    <h3>Plant Hire</h3>
    <p>Lorem ipsum dolor sit amet, consectetur adipiscing elit. Cras dapibus vehicula tortor, maximus sollicitudin ligula luctus a.</p>
    <span class="more">Learn More ›</span>
  </div>
  <div class="service-card cta" style="left:771px;top:403px">
    <div class="small">Connect with</div>
    <h3>Excavation &amp;<br>Earthmoving Experts</h3>
    <a class="btn btn-white">Get Started ›</a>
  </div>
</section>

<section class="testimonials">
  <div class="photo" role="img" aria-label="Dark quarry site with excavator in the background"></div>
  <h2 class="section-title display">What our clients say</h2>
  <div class="review" style="left:121px">
    <div class="avatar" role="img" aria-label="Client portrait"></div>
    <div class="stars">★★★★★</div>
    <h4>Marcus Whitfield</h4>
    <p>Lorem ipsum dolor sit amet, consectetur adipiscing elit, sed do eiusmod tempor in cididunt ut labore et dolore magna aliqua. Quis ipsum suspendisse ultrices gravida. Risus commodo viverra maecenas ac cumsan lacus vel facilisis.</p>
  </div>
  <div class="review" style="left:446px">
    <div class="avatar" role="img" aria-label="Client portrait"></div>
    <div class="stars">★★★★★</div>
    <h4 style="text-transform:none">Priya &amp; Tom</h4>
    <p>Lorem ipsum dolor sit amet, consectetur adipiscing elit, sed do eiusmod tempor in cididunt ut labore et dolore magna aliqua. Quis ipsum suspendisse ultrices gravida. Risus commodo viverra maecenas ac cumsan lacus vel facilisis.</p>
  </div>
  <div class="review" style="left:771px">
    <div class="avatar" role="img" aria-label="Client portrait"></div>
    <div class="stars">★★★★★</div>
    <h4 style="text-transform:none">Ellen Marsh</h4>
    <p>Lorem ipsum dolor sit amet, consectetur adipiscing elit, sed do eiusmod tempor in cididunt ut labore et dolore magna aliqua. Quis ipsum suspendisse ultrices gravida. Risus commodo viverra maecenas ac cumsan lacus vel facilisis.</p>
  </div>
</section>

<section class="gallery">
  <h2 class="section-title display">Projects Gallery</h2>
  <div class="tile" style="left:121px;top:144px;width:472px;height:255px;background:linear-gradient(160deg,#8a7560 0%,#c2a585 50%,#9a8068 100%)" role="img" aria-label="Quarry with excavator loading trucks"><span>Bulk Excavation</span></div>
  <div class="tile" style="left:605px;top:144px;width:474px;height:255px;background:linear-gradient(180deg,#6f8fb8 0%,#aab8c8 45%,#d2a474 70%,#b9875a 100%)" role="img" aria-label="Orange excavator on sandy ground"><span>Detailed Excavation</span></div>
  <div class="tile" style="left:121px;top:412px;width:244px;height:255px;background:linear-gradient(160deg,#4a5a6a 0%,#7a7f85 50%,#a08868 100%)" role="img" aria-label="Excavator demolishing a building"><span>Demolition</span></div>
  <div class="tile" style="left:378px;top:412px;width:443px;height:255px;background:linear-gradient(180deg,#8ea8c4 0%,#7d8894 50%,#8a7a48 100%)" role="img" aria-label="Workers installing shoring steel"><span>Shoring</span></div>
  <div class="tile" style="left:834px;top:412px;width:245px;height:255px;background:linear-gradient(180deg,#d8e2ea 0%,#c9a44a 60%,#8a8a5a 100%)" role="img" aria-label="Yellow excavator parked on site"><span>Plant Hire</span></div>
  <a class="btn">View All Project ↗</a>
</section>

<section class="cta-band">
  <h2 class="display">Start your new journey<br>with Harbourgate Earthmoving</h2>
  <a class="btn btn-white">Contact Us</a>
</section>

<footer class="site-footer">
  <div class="brand">Harbourgate Earthmoving</div>
  <p class="about-text">Lorem ipsum dolor sit amet, consectetur adipiscing elit. Cras dapibus vehicula tortor, maximus sollicitudin ligula luctus a. Duis molestie mauris ac nunc tincidunt</p>
  <div class="socials" aria-label="Social links"><span></span><span></span><span></span><span></span></div>

  <div class="foot-col" style="left:427px">
    <h5>Navigation</h5>
    <ul><li>Home</li><li>About Us</li><li>Services</li><li>Gallery</li><li>Contact</li></ul>
  </div>
  <div class="foot-col" style="left:608px;width:205px">
    <h5>Contact Us</h5>
    <p>14 Wharf Road Unit 3<br>Rozelle, NSW 2039 Australia</p>
    <p>(02) 9555 0148</p>
    <p class="mail">office@harbourgateearthmoving.com</p>
    <p>Monday – Friday<br>8:00 AM – 4:00 PM</p>
  </div>
  <div class="foot-col" style="left:828px">
    <h5>Subscribe Newsletter</h5>
    <div>Subscribe to our newsletter</div>
    <div class="news-input">Enter your email</div>
    <a class="btn">Subscribe</a>
  </div>

  <div class="copyright">© 2025 Copyright - Harbourgate Earthmoving - Website by Brightline Studio</div>
  <div class="foot-deco" aria-hidden="true">Harbourgate Earthmoving</div>
</footer>

</body>
</html>
```